Website Design for Forklift Training Company

DO NOT CONTACT PRIVATELY. ONLY SUBMISSIONS HERE WILL BE CONSIDERED

I need a design for a website that offers forklift training courses.

The company offers accredited, onsite forklift training that are customized for the needs of each individual company. The company offers a variety of courses to operate forklifts and other machinary.

About: "Pembrook Lift Academy Ltd delivers bespoke onsite forklift truck operator training throught the uk.
All our instructors have a wealth of knowledge and expertise to provide your company with all your forklift truck training requirements.
Pembrook Lift Academy Ltd is registered and accredited by qkmvd standards so you can be rest assured that all forklift training is carried out the very highest standard"

I need the following pages designed:
> a) Home Page: Include a header image, ways to contact, about snippet, overview of courses, accreditation that will be received after completing the courses. (See attachments for samples)
> b) About Page
> c) Contact Us Page
> d) Course Page Template: A page that will be used as template for the courses offered. It should contain;
1. Cover image for the course
2. A description of the course
3. A table indicating the various course options
4. Course Objectives
5. What the trainee will receive after doing the course (example: a certification)

Target Market(s)

Industrial Businesses

Number of Pages Required

4 page

Colors
0054AA
0677BA
7BADD7
CADEEF
E8F1F8
0094D4
00A9DD
6FCCEA
C7EBF8
E9F6FB

Requirements
Should not have
• - No Search bar

```html
<!DOCTYPE html>
<html lang="en">
<head>
<meta charset="utf-8">
<title>Pembrook Lift Academy Ltd – Forklift Training</title>
<link href="https://fonts.googleapis.com/css2?family=Oswald:wght@500;600&family=Roboto:wght@400;500;700&display=swap" rel="stylesheet">
<style>
:root{
  --blue:#0054AA;
  --blue-mid:#0677BA;
  --sky:#6FCCEA;
  --frame:#7BC8E6;
  --pale:#E9F6FB;
  --ink:#111;
  --text:#666;
  --footer:#1b1b1b;
  --white:#fff;
}
*{margin:0;padding:0;box-sizing:border-box}
html,body{width:1200px;height:3716px;overflow:hidden}
body{font-family:'Roboto',sans-serif;color:var(--text);position:relative;background:var(--white)}
.abs{position:absolute}
.h-display{font-family:'Oswald',sans-serif;font-weight:600;color:var(--ink);text-transform:uppercase}
.btn{position:absolute;background:var(--blue);color:var(--white);font-weight:700;font-size:15px;display:flex;align-items:center;justify-content:center;text-transform:uppercase;letter-spacing:.2px}

/* hero */
.hero{position:absolute;left:0;top:0;width:1200px;height:617px;background:linear-gradient(100deg,#2a2b2e 0%,#4a3a26 40%,#6b5530 60%,#2e2a22 100%)}
.hero::after{content:"";position:absolute;inset:0;background:linear-gradient(90deg,rgba(0,0,0,.45),rgba(0,0,0,.1))}
.nav{position:absolute;left:111px;top:37px;width:797px;height:77px;background:var(--white);z-index:2;display:flex;align-items:center}
.brand{margin-left:25px;display:flex;align-items:center;gap:10px;font-weight:700;font-size:15px;color:var(--ink);width:220px;line-height:1.1}
.brand i{width:40px;height:40px;background:#111;display:block;flex:none}
.menu{display:flex;gap:22px;font-size:14px;font-weight:500;color:var(--ink);margin-left:20px}
.nav-phone{position:absolute;left:908px;top:37px;width:181px;height:77px;background:var(--blue);z-index:2;color:var(--white);font-weight:700;font-size:17px;display:flex;align-items:center;justify-content:center;gap:10px}
.hero-copy{position:absolute;left:111px;top:268px;z-index:2;color:var(--white)}
.hero-copy h1{font-family:'Oswald',sans-serif;font-weight:600;font-size:42px;line-height:1.3;text-transform:uppercase}
.hero-copy p{font-size:15px;font-weight:500;line-height:26px;width:540px;margin-top:10px}
.arrow{position:absolute;top:309px;width:37px;height:37px;z-index:2;display:flex;align-items:center;justify-content:center}

/* about */
.about-frame{left:111px;top:712px;width:464px;height:365px;border:7px solid var(--frame);border-right:none;border-bottom:none}
.about-frame::after{content:"";position:absolute;left:-7px;bottom:0;width:7px;height:0}
.about-photo{left:137px;top:737px;width:466px;height:368px;background:var(--white);box-shadow:0 4px 14px rgba(0,0,0,.12);padding:7px}
.about-photo div{width:100%;height:100%;background:linear-gradient(160deg,#6b7d8c,#c8b23a 55%,#3f4a3a)}
.about-title{left:639px;top:746px;font-size:40px}
.about-text{left:639px;top:823px;width:450px;font-size:15px;line-height:25.7px;text-align:justify}

/* courses */
.courses{left:0;top:1200px;width:1200px;height:1028px;background:var(--pale)}
.sec-title{position:absolute;left:0;width:1200px;text-align:center;font-size:34px}
.courses-lead{left:160px;top:1318px;width:880px;text-align:center;font-size:14px;line-height:24px}
.tab{position:absolute;top:1425px;height:49px;background:var(--white);color:var(--blue);font-weight:700;font-size:14px;display:flex;align-items:center;justify-content:center;box-shadow:0 2px 6px rgba(0,0,0,.06)}
.tab.on{background:var(--blue);color:var(--white)}
.card{position:absolute;width:313px;height:265px;background:var(--white);padding:6px;box-shadow:0 2px 8px rgba(0,0,0,.06)}
.card .ph{height:204px}
.card h3{text-align:center;color:var(--blue);font-size:17px;font-weight:500;margin-top:18px}
.card.feature{background:linear-gradient(rgba(0,84,170,.88),rgba(0,84,170,.9)),linear-gradient(135deg,#2a4f7a,#0a2c5a);color:var(--white);text-align:center;padding:30px 22px}
.card.feature h3{color:var(--white);margin:0;font-size:18px}
.card.feature hr{width:90px;border:none;border-top:2px solid var(--white);margin:14px auto 18px}
.card.feature p{font-size:14px;line-height:24px}
.card.feature b{display:block;margin-top:14px;font-size:14px}

/* accreditation */
.acc-card{position:absolute;top:2467px;width:473px;height:323px;background:var(--white);box-shadow:0 2px 12px rgba(0,0,0,.1);text-align:center;padding:92px 22px 0;font-size:14px;line-height:23px}
.badge{position:absolute;top:2408px;width:166px;height:117px;border:5px solid var(--frame);background:var(--white);display:flex;align-items:center;justify-content:center}
.badge span{display:block;width:74px;height:74px;background:#1a2470}
.badge span.alt{width:100px;height:48px;background:#2b3990;border-radius:6px}

/* contact */
.contact{left:0;top:2888px;width:1200px;height:509px;background:var(--pale)}
.info{position:absolute;left:134px;display:flex;gap:25px}
.info .ic{width:64px;height:64px;border-radius:50%;background:var(--white);box-shadow:0 2px 10px rgba(0,0,0,.1);display:flex;align-items:center;justify-content:center;flex:none}
.info h4{color:var(--blue);font-size:17px;font-weight:700;margin-top:-8px}
.info p{font-size:14px;line-height:24px;color:#444;margin-top:6px}
.field{position:absolute;background:var(--white);border:1px solid #dde6ec;font-size:14px;color:#777;display:flex;align-items:center;gap:8px;padding-left:18px}
.field.area{align-items:flex-start;padding-top:18px}

/* footer */
.footer{left:0;top:3397px;width:1200px;height:319px;background:var(--footer);color:var(--white)}
.f-logo{position:absolute;left:111px;top:3455px;display:flex;align-items:center;gap:10px;font-weight:700;font-size:17px;width:280px}
.f-logo i{width:82px;height:72px;background:var(--white);display:block}
.social{position:absolute;top:3567px;width:35px;height:35px;background:var(--blue)}
.social.w{background:var(--white)}
.f-col{position:absolute;top:3452px;font-size:15px;line-height:26px}
.f-col h5{font-size:16px;font-weight:700;margin-bottom:16px}
.f-contact li{list-style:none;display:flex;gap:16px;margin-bottom:10px}
.f-rule{left:111px;top:3654px;width:978px;height:1px;background:#555}
.copy{left:0;top:3670px;width:1200px;text-align:center;font-size:13px}
.chat{left:1124px;top:3611px;width:35px;height:35px;background:var(--white)}
</style>
</head>
<body>

<!-- Hero -->
<section class="hero" role="img" aria-label="Photo of an operator in a hard hat driving a forklift outside a warehouse"></section>
<header class="nav">
  <div class="brand"><i></i>Pembrook Lift Academy Ltd</div>
  <nav class="menu"><span>HOME</span><span>ABOUT US</span><span>TRAINING COURSES ⌄</span><span>PRICES</span><span>CONTACT US</span></nav>
</header>
<div class="nav-phone">
  <svg width="16" height="16" viewBox="0 0 24 24" fill="#fff"><path d="M6.6 10.8a15.1 15.1 0 0 0 6.6 6.6l2.2-2.2a1 1 0 0 1 1-.25 11.4 11.4 0 0 0 3.6.57 1 1 0 0 1 1 1V20a1 1 0 0 1-1 1A17 17 0 0 1 3 4a1 1 0 0 1 1-1h3.5a1 1 0 0 1 1 1c0 1.25.2 2.45.57 3.57a1 1 0 0 1-.25 1z"/></svg>
  07700900123
</div>
<div class="arrow" style="left:35px;background:#fff"><svg width="14" height="20" viewBox="0 0 14 20"><path d="M11 2 3 10l8 8" stroke="#111" stroke-width="2.5" fill="none"/></svg></div>
<div class="arrow" style="left:1128px;background:var(--blue)"><svg width="14" height="20" viewBox="0 0 14 20"><path d="m3 2 8 8-8 8" stroke="#fff" stroke-width="2.5" fill="none"/></svg></div>
<div class="hero-copy">
  <h1>Pembrook Forklift Training Courses</h1>
  <p>The company offers accredited, onsite forklift training that are customized for the needs of each individual company.</p>
</div>
<div class="btn" style="left:111px;top:404px;width:153px;height:49px;z-index:2">Get Started</div>

<!-- About -->
<div class="abs about-frame"></div>
<div class="abs" style="left:111px;top:712px;width:7px;height:365px;background:var(--frame)"></div>
<div class="abs" style="left:111px;top:1070px;width:30px;height:7px;background:var(--frame)"></div>
<div class="abs about-photo"><div role="img" aria-label="Photo of two instructors in hard hats and hi-vis vests beside a forklift"></div></div>
<h2 class="abs h-display about-title">About Us</h2>
<p class="abs about-text">Pembrook Lift Academy Ltd delivers bespoke onsite forklift truck operator training throught the uk. All our instructors have a wealth of knowledge and expertise to provide your company with all your forklift truck training requirements. Pembrook Lift Academy Ltd is registered and accredited by qkmvd standards so you can be rest assured that all forklift training is carried out the very highest standard</p>
<div class="btn" style="left:639px;top:1017px;width:141px;height:47px">Learn More</div>

<!-- Courses -->
<section class="abs courses"></section>
<h2 class="sec-title h-display" style="top:1250px">Forklift Training Courses</h2>
<p class="abs courses-lead">We specialise in onsite forklift training using the equipment and facilities your employees will use in there everyday work wether its counterbalance morrant halvo cherry picker to name a few. We also accommodate an anytime any shift training schedule to cater for your different shift patterns.By the time we have finished your staff will be well trained and ready to operate efficiently and safely</p>
<div class="tab on" style="left:222px;width:242px">FORKLIFT TRAINING COURSES</div>
<div class="tab" style="left:477px;width:244px">MEWP TRAINING COURSES</div>
<div class="tab" style="left:735px;width:243px">OTHER TRAINING COURSES</div>

<div class="card" style="left:111px;top:1517px"><div class="ph" role="img" aria-label="Photo of an instructor guiding a trainee on a narrow aisle truck" style="background:linear-gradient(135deg,#8a9aa8,#e07a2a 55%,#5a6470)"></div><h3>Benton Truck Training Course</h3></div>
<div class="card feature" style="left:443px;top:1517px">
  <h3>Cormac Lift Training course</h3><hr>
  <p>Cormac lift Forklifts are essential in the workplace and are operated throughout the world in warehouses, stores, construction sites, factories and many more places.</p>
  <b>Learn More &nbsp; »</b>
</div>
<div class="card" style="left:774px;top:1517px"><div class="ph" role="img" aria-label="Photo of a yellow counterbalance forklift in a warehouse" style="background:linear-gradient(160deg,#b08560,#c9c9c4 50%,#d9c02a 75%,#666)"></div><h3>Counterbalance Training Course</h3></div>
<div class="card" style="left:111px;top:1801px"><div class="ph" role="img" aria-label="Photo of a trainee on a reach truck with an instructor holding a clipboard" style="background:linear-gradient(135deg,#6f7f8e,#d8562a 45%,#cfd23a 75%,#7a8088)"></div><h3>Flexor Truck Training Course</h3></div>
<div class="card" style="left:443px;top:1801px"><div class="ph" role="img" aria-label="Photo of a truck mounted loader crane lifting a load" style="background:linear-gradient(180deg,#c7cbcf,#8e949a 60%,#4e5358)"></div><h3>Halvo Crane Training Course</h3></div>
<div class="card" style="left:774px;top:1801px"><div class="ph" role="img" aria-label="Photo of workers in hi-vis vests beside a low level order picker" style="background:linear-gradient(160deg,#c8cdd2,#9aa3ab 50%,#c8d43a 70%,#7d8790)"></div><h3>Llop Training Course</h3></div>
<div class="btn" style="left:506px;top:2120px;width:186px;height:47px">View All Courses</div>

<!-- Accreditation -->
<h2 class="sec-title h-display" style="top:2312px">Forklift Training Accreditation</h2>
<div class="acc-card" style="left:111px">qkmvd is recognised throughout the united kingdom and Ireland as one of the leading material handling equipment training accrediting bodies.qkmvd is a founder member of the CWTA (accrediting bodies association for workplace transport) and this replaced the accrediting bodies forum previously run by the NSA.</div>
<div class="acc-card" style="left:614px">We are accredited by the qkmvd who are recognised by the national safety authority as competent to deliver forklift truck operator training courses. As an qkmvd accredited training provider we are monitored annually to ensure we are maintaining our high standards as laid down by the qkmvd.</div>
<div class="badge" style="left:265px" role="img" aria-label="Accreditation badge"><span></span></div>
<div class="badge" style="left:768px" role="img" aria-label="Association badge"><span class="alt"></span></div>
<div class="btn" style="left:281px;top:2704px;width:133px;height:46px">Read More</div>
<div class="btn" style="left:784px;top:2704px;width:134px;height:46px">Read More</div>

<!-- Contact -->
<section class="abs contact"></section>
<h2 class="sec-title h-display" style="top:2928px">Get In Touch</h2>
<div class="info" style="top:3005px">
  <div class="ic"><svg width="26" height="30" viewBox="0 0 24 28" fill="none" stroke="#0054AA" stroke-width="1.8"><path d="M12 26s9-8.5 9-15a9 9 0 0 0-18 0c0 6.5 9 15 9 15z"/><circle cx="12" cy="11" r="3.5"/></svg></div>
  <div><h4>LOCATION</h4><p>14 Harrow Lane Ashby Fields<br>Kettleby KT4 7RW</p></div>
</div>
<div class="info" style="top:3105px">
  <div class="ic"><svg width="28" height="28" viewBox="0 0 24 24" fill="none" stroke="#0054AA" stroke-width="1.6"><path d="M6.6 10.8a15.1 15.1 0 0 0 6.6 6.6l2.2-2.2a1 1 0 0 1 1-.25 11.4 11.4 0 0 0 3.6.57 1 1 0 0 1 1 1V20a1 1 0 0 1-1 1A17 17 0 0 1 3 4a1 1 0 0 1 1-1h3.5a1 1 0 0 1 1 1c0 1.25.2 2.45.57 3.57a1 1 0 0 1-.25 1z"/><path d="M15 3a6 6 0 0 1 6 6M15 6.5a2.5 2.5 0 0 1 2.5 2.5"/></svg></div>
  <div><h4>CALL US</h4><p>07700900123</p></div>
</div>
<div class="info" style="top:3193px">
  <div class="ic"><svg width="34" height="26" viewBox="0 0 34 26" fill="none" stroke="#0054AA" stroke-width="1.8"><rect x="1" y="1" width="32" height="24"/><path d="m1 1 16 13L33 1M1 25l12-11M33 25 21 14"/></svg></div>
  <div><h4>EMAIL US</h4><p>info@pembrooklift.example</p></div>
</div>
<div class="field" style="left:499px;top:3012px;width:289px;height:49px"><svg width="12" height="13" viewBox="0 0 12 13" fill="#888"><circle cx="6" cy="3.5" r="3.2"/><path d="M0 13c0-4 2.5-6 6-6s6 2 6 6z"/></svg>First Name</div>
<div class="field" style="left:799px;top:3012px;width:288px;height:49px"><svg width="12" height="13" viewBox="0 0 12 13" fill="#888"><circle cx="6" cy="3.5" r="3.2"/><path d="M0 13c0-4 2.5-6 6-6s6 2 6 6z"/></svg>Last Name</div>
<div class="field" style="left:499px;top:3079px;width:289px;height:49px"><svg width="13" height="13" viewBox="0 0 24 24" fill="#888"><path d="M6.6 10.8a15.1 15.1 0 0 0 6.6 6.6l2.2-2.2a1 1 0 0 1 1-.25 11.4 11.4 0 0 0 3.6.57 1 1 0 0 1 1 1V20a1 1 0 0 1-1 1A17 17 0 0 1 3 4a1 1 0 0 1 1-1h3.5a1 1 0 0 1 1 1c0 1.25.2 2.45.57 3.57a1 1 0 0 1-.25 1z"/></svg>Your Phone</div>
<div class="field" style="left:799px;top:3079px;width:288px;height:49px"><svg width="14" height="11" viewBox="0 0 14 11" fill="none" stroke="#888" stroke-width="1.3"><rect x=".7" y=".7" width="12.6" height="9.6"/><path d="m.7.7 6.3 5 6.3-5"/></svg>Your Email</div>
<div class="field area" style="left:499px;top:3145px;width:588px;height:110px"><svg width="14" height="12" viewBox="0 0 14 12" fill="#888"><ellipse cx="7" cy="5" rx="7" ry="5"/><path d="M2 8 1 12l4-3z"/></svg>How Can we help you?</div>
<div class="btn" style="left:499px;top:3296px;width:153px;height:50px;gap:12px">Submit <svg width="16" height="16" viewBox="0 0 16 16" fill="#fff"><path d="M16 0 0 7l5 2 1 6 3-4 4 3z"/></svg></div>

<!-- Footer -->
<footer class="abs footer"></footer>
<div class="f-logo"><i></i>Pembrook Lift Academy Ltd</div>
<div class="social" style="left:174px" role="img" aria-label="Social link"></div>
<div class="social w" style="left:222px" role="img" aria-label="Social link"></div>
<div class="social w" style="left:270px" role="img" aria-label="Social link"></div>
<div class="f-col" style="left:459px"><h5>OUR COMPANY</h5>Home<br>About us<br>Training Courses<br>Prices<br>Contact Us</div>
<div class="f-col" style="left:665px"><h5>OTHER LINKS</h5>Site map<br>Privacy Policy<br>Terms Of Use<br>Legal Support</div>
<div class="f-col f-contact" style="left:865px"><h5>CONTACT US</h5>
  <ul>
    <li><svg width="10" height="14" viewBox="0 0 10 14" fill="#0677BA" style="margin-top:6px"><path d="M5 14S0 8.5 0 5a5 5 0 0 1 10 0c0 3.5-5 9-5 9z"/></svg><span>14 Harrow Lane Ashby Fields<br>Kettleby KT4 7RW</span></li>
    <li><svg width="12" height="12" viewBox="0 0 24 24" fill="#0677BA" style="margin-top:7px"><path d="M6.6 10.8a15.1 15.1 0 0 0 6.6 6.6l2.2-2.2a1 1 0 0 1 1-.25 11.4 11.4 0 0 0 3.6.57 1 1 0 0 1 1 1V20a1 1 0 0 1-1 1A17 17 0 0 1 3 4a1 1 0 0 1 1-1h3.5a1 1 0 0 1 1 1c0 1.25.2 2.45.57 3.57a1 1 0 0 1-.25 1z"/></svg><span>07700900123</span></li>
    <li><svg width="13" height="10" viewBox="0 0 13 10" fill="#0677BA" style="margin-top:8px"><rect width="13" height="10"/></svg><span>info@pembrooklift.example</span></li>
  </ul>
</div>
<div class="abs f-rule"></div>
<p class="abs copy">© 2021 Company Name. All Rights Reserved</p>
<div class="abs chat" role="img" aria-label="Chat button"></div>

</body>
</html>
```